Design a Brochure for IT Cloud company

This is an open idea type brochure design. I will attach our logo so that there's relevance, and brochure text to be arranged and placed in arrangement that your design will produce.....Ideally I would like a tri-fold brochure if possible [login to view URL]

```html
<!DOCTYPE html>
<html lang="en">
<head>
<meta charset="utf-8">
<title>Nimbrix – Tri-fold Brochure</title>
<link rel="stylesheet" href="https://fonts.googleapis.com/css2?family=Open+Sans:wght@300;400;600;700&display=swap">
<style>
  :root {
    --page-bg: #2b2d31;
    --paper: #ffffff;
    --teal: #2bb3c9;
    --teal-dark: #1a8fa3;
    --ink: #2f3338;
    --ink-soft: #5d636b;
    --grey-band: #e4e5e7;
    --grey-deep: #cfd1d4;
    --mist: #d3dae6;
    --photo-dark: #2d3b52;
    --photo-mid: #6f84a3;
    --photo-light: #b9c8dc;
  }
  * { box-sizing: border-box; margin: 0; padding: 0; }
  html, body { width: 1200px; height: 981px; overflow: hidden; }
  body {
    background: var(--page-bg);
    font-family: "Open Sans", Arial, sans-serif;
    color: var(--ink);
  }
  .brochure {
    position: absolute;
    left: 45px; top: 60px;
    width: 1110px; height: 860px;
    background: var(--paper);
    overflow: hidden;
  }
  .brochure-art { position: absolute; inset: 0; }
  .block { position: absolute; }

  /* Core business */
  .core-heading { left: 150px; top: 30px; text-transform: uppercase; }
  .core-heading .lead { display: block; color: var(--teal); font-weight: 300; font-size: 30px; letter-spacing: 2px; line-height: 1; }
  .core-heading .tail { display: block; color: var(--ink-soft); font-weight: 400; font-size: 15px; letter-spacing: 7px; margin-top: 4px; }
  .core-list { left: 40px; top: 100px; list-style: none; width: 320px; }
  .core-list li { display: flex; align-items: center; height: 44px; font-size: 10px; text-transform: uppercase; color: var(--ink); }
  .core-list li .dot { width: 32px; height: 32px; border-radius: 50%; background: var(--photo-mid); border: 2px solid var(--paper); margin-right: 10px; flex: none; }
  .core-list li strong { font-weight: 700; margin-right: 3px; }
  .core-list li.extra { justify-content: flex-end; font-weight: 700; height: 28px; }

  /* Solutions */
  .solutions { left: 40px; top: 340px; width: 310px; }
  .solutions h2 { color: var(--teal); font-weight: 300; font-size: 24px; letter-spacing: 3px; text-transform: uppercase; line-height: 1.05; }
  .solutions h3 { color: var(--ink); font-weight: 400; font-size: 17px; letter-spacing: 1px; text-transform: uppercase; margin-bottom: 10px; }
  .solutions h4 { font-size: 14px; font-weight: 600; margin-bottom: 6px; }
  .solutions p.ask { font-size: 12px; font-weight: 700; margin-bottom: 4px; }
  .solutions ul { list-style: none; font-size: 12px; line-height: 1.4; }
  .solutions ul li::before { content: "• "; color: var(--ink); }
  .solutions-copy { left: 40px; top: 720px; width: 170px; font-size: 9.5px; line-height: 1.45; color: var(--ink-soft); }

  /* About */
  .about { left: 400px; top: 80px; width: 310px; }
  .about h2 { font-size: 18px; font-weight: 400; letter-spacing: 1px; text-transform: uppercase; margin-bottom: 10px; }
  .about h2 strong { font-weight: 700; }
  .about p { font-size: 10px; line-height: 1.55; color: var(--ink-soft); }

  /* Contact */
  .contact { left: 430px; top: 690px; width: 290px; text-align: right; font-size: 9.5px; line-height: 1.6; color: var(--ink-soft); text-transform: uppercase; }
  .contact .gap { margin-top: 10px; }
  .contact .label { color: var(--teal); font-weight: 600; }

  /* Brand */
  .brand { left: 790px; top: 690px; width: 300px; }
  .brand-name { display: flex; align-items: center; gap: 10px; font-size: 44px; font-weight: 700; color: var(--ink-soft); line-height: 1; }
  .brand-name .mark { width: 22px; height: 22px; border-radius: 50%; background: var(--teal); }
  .brand-tagline { font-size: 19px; font-weight: 400; color: var(--ink); margin-top: 6px; }
</style>
</head>
<body>
<main class="brochure">
  <svg class="brochure-art" width="1110" height="860" viewBox="0 0 1110 860" xmlns="http://www.w3.org/2000/svg">
    <defs>
      <linearGradient id="hands-tone" x1="0" y1="0" x2="1" y2="1">
        <stop offset="0" stop-color="#e9edf2"/>
        <stop offset="0.45" stop-color="var(--photo-mid)"/>
        <stop offset="1" stop-color="var(--photo-dark)"/>
      </linearGradient>
      <radialGradient id="cloud-tone" cx="0.45" cy="0.45" r="0.6">
        <stop offset="0" stop-color="var(--photo-light)"/>
        <stop offset="0.6" stop-color="var(--photo-mid)"/>
        <stop offset="1" stop-color="var(--photo-dark)"/>
      </radialGradient>
    </defs>
    <!-- panel bands -->
    <polygon class="band-top" points="110,0 370,0 370,70 0,300 0,70" fill="var(--grey-band)"/>
    <polygon class="band-top-edge" points="0,300 370,70 370,95 0,325" fill="var(--grey-deep)" opacity="0.5"/>
    <polygon class="band-lower" points="0,690 560,590 560,640 0,740" fill="var(--mist)" opacity="0.7"/>
    <polygon class="panel-mist" points="740,520 1110,390 1110,860 740,860" fill="var(--mist)"/>
    <polygon class="panel-mist-mid" points="560,590 740,520 740,860 560,860" fill="var(--mist)" opacity="0"/>
    <!-- photo band -->
    <polygon class="photo-hands" role="img" aria-label="Photo: businessman's hands holding a small cloud shape" points="0,560 560,455 560,600 0,705" fill="url(#hands-tone)"/>
    <!-- fold lines -->
    <line x1="370" y1="0" x2="370" y2="860" stroke="#000" stroke-opacity="0.06"/>
    <line x1="740" y1="0" x2="740" y2="860" stroke="#000" stroke-opacity="0.06"/>
    <!-- feature circle -->
    <circle cx="730" cy="440" r="178" fill="var(--teal)"/>
    <circle class="photo-cloud" role="img" aria-label="Photo: person touching a cloud network of connected service icons" cx="730" cy="440" r="164" fill="url(#cloud-tone)"/>
  </svg>

  <h1 class="block core-heading"><span class="lead">Our Core</span><span class="tail">Business</span></h1>
  <ul class="block core-list">
    <li><span class="dot"></span><strong>Cloud Computing</strong></li>
    <li><span class="dot"></span><strong>Online Desktop</strong> as a Service DaaS</li>
    <li><span class="dot"></span><strong>Infrastructure</strong> as a Service IaaS</li>
    <li><span class="dot"></span><strong>Disaster Recovery</strong> as a Service DRaaS</li>
    <li><span class="dot"></span><strong>Backup</strong> as a Service BaaS</li>
    <li class="extra">Integration / Support</li>
  </ul>

  <section class="block solutions">
    <h2>Our Solutions</h2>
    <h3>To your IT challenges</h3>
    <h4>Online Desktop</h4>
    <p class="ask">Do you want to stop agonising about:</p>
    <ul>
      <li>Your email systems and compliance?</li>
      <li>Your server hardware warranty?</li>
      <li>Your desktop software and patching levels?</li>
      <li>Software licensing?</li>
    </ul>
  </section>
  <p class="block solutions-copy">If you do, the Online Desktop is for you. Your files and apps live in one secure place you can reach from any device. We handle updates, backups and licences, so your staff can focus on their work.</p>

  <section class="block about">
    <h2>About <strong>Us</strong></h2>
    <p>Nimbrix Enterprise Systems is a privately owned company that provides cloud hosting technology solutions across a wide range of industries throughout Australia and Asia Pacific. Based in Sydney, our team designs, builds and manages secure platforms for growing firms. We pair deep technical skill with plain advice, so clients get systems that scale, stay safe and cost less to run. From planning to daily support, we stay with you.</p>
  </section>

  <address class="block contact">
    <div>Phone – 1800 000 000</div>
    <div class="gap">www.nimbrix.example</div>
    <div class="gap">Level 12, 40 Harbour Rd</div>
    <div>Northbank NSW 2000</div>
    <div>Australia</div>
    <div class="gap"><span class="label">Distributors:</span> Unit 4, 18 Dale Street, Eastvale</div>
  </address>

  <div class="block brand">
    <div class="brand-name"><span>Nimbrix</span><span class="mark"></span></div>
    <div class="brand-tagline">Tagline goes here if any</div>
  </div>
</main>
</body>
</html>
```